4x6 Postcard Design Full Color Double Sided

Hello, I am in need of a postcard design. The document with details is attached. And I am writing here also:

To My Dear Colleague,

This week, I want you to do yourself and me a favor, okay?

I want you to ask your boss for a $100,000 per year salary increase. If the answer is no then I want you to “give yourself” a

$10,000 per month pay increase RIGHT NOW!

The opportunity to make 6-7 figures using SIMPLE online systems is exploding right before your eyes. Why aren’t you paying attention? Is It because you don’t have any idea how to earn money online? Or are you intimidated by the thought of it because you’re not tech-savvy?

Throw any negative thoughts out of your mind and let us help you build a $100,000 + yearly income that runs on automatic. We’re not promising a million dollars overnight or that you’ll be able to quit your job tomorrow, BUT if an extra $10,000 per month would help you reach your goals, then you should take action today!

OUR SIMPLE IS SO EASY TO USE, A FIFTH GRADER COULD BE SUCCESSFUL!

We’re so sure you will be successful with our system that we are inviting you to
GET STARTED TODAY FOR FREE!!!

That’s right…for FREE! No credit card is required.

GO SIGN UP NOW:
www.qmvhub.com/joinFREE
Enter Referral ID#

KV-R8057

Free offer expires in 48 hours!!!

Instructions for designers:
I’d like the color scheme to stay consistent with my company’s color scheme. To see the color scheme of Blue Lark Gains go to www.qmvhub.com
As you are reading the text, please make certain parts of the text be emphasized on the postcard – wherever you feel necessary. When you read it, what would catch your attention? Those parts are the parts I’d like you to emphasize on the card by making them bolder, or a different color, or larger or highlighted.

The postcard is a 4x6 card, double-sided, full color

The text above is for the front side. The back will be the same thing, except in the spot where I have KV-R8057. On the backside it should say: (Use ID# on reverse side)

It’s like you are really only designing a one-sided card because the back side is almost an exact duplicate.

Thank you, you rock! =)

Target Market(s)

work from home seekers / make money online enthusiasts

Font styles to use
Serif

Requirements
Must have
• Color scheme similar to the color scheme at www.qmvhub.com
• The rest of the requirements are attached to the word doc.
• I will also send the logo, but it wouldn't let me upload because the file is too large.
Nice to have
• I really I am looking for something that really looks clean, but attention-grabbing

```html
<!DOCTYPE html>
<html lang="en">
<head>
<meta charset="utf-8">
<title>Blue Lark Gains – Postcard Front and Back</title>
<link rel="stylesheet" href="https://fonts.googleapis.com/css2?family=Mulish:wght@400;700;800&family=Roboto+Condensed:wght@400;700&family=Lato:wght@700&display=swap">
<style>
  :root{
    --stage-light:#cfcfcf;
    --stage-dark:#858585;
    --band-deep:#3c7fa6;
    --band-mid:#5d9ec2;
    --band-pale:#8fbdd6;
    --wedge:#5bbde0;
    --disc:#3a90b8;
    --disc-ring:#b5e3f2;
    --heading-blue:#3b84a8;
    --accent-blue:#4fb3dc;
    --button:#2f7ea2;
    --ink:#1f1f1f;
    --white:#ffffff;
  }
  *{margin:0;padding:0;box-sizing:border-box}
  html,body{width:1200px;height:1200px;overflow:hidden}
  body{
    background:radial-gradient(ellipse at 50% 45%,var(--stage-light) 0%,#a9a9a9 55%,var(--stage-dark) 100%);
    position:relative;
    font-family:"Mulish",sans-serif;
    color:var(--ink);
  }
  .side-label{
    position:absolute;
    font-family:"Mulish",sans-serif;
    font-weight:800;
    font-size:38px;
    color:var(--white);
    letter-spacing:1px;
  }
  .side-label--front{left:989px;top:512px}
  .side-label--back{left:152px;top:1091px}

  .postcard{
    position:absolute;
    width:676px;height:524px;
    background:var(--white);
    overflow:hidden;
    box-shadow:0 4px 10px rgba(0,0,0,.35);
  }
  .postcard--front{left:285px;top:48px}
  .postcard--back{left:288px;top:626px}
  .postcard__shapes{position:absolute;inset:0}

  .postcard__letter{
    position:absolute;left:19px;
    color:var(--white);
    font-size:13.4px;
    line-height:16px;
    white-space:nowrap;
  }
  .postcard__greeting{top:48px}
  .postcard__favor{top:80px}
  .postcard__ask{top:112px}
  .postcard__headline{
    position:absolute;left:19px;top:151px;
    color:var(--white);
    font-weight:800;
    font-size:19.5px;
    white-space:nowrap;
  }

  .brand{
    position:absolute;left:428px;top:36px;
    display:flex;align-items:center;gap:10px;
  }
  .brand__dot{width:22px;height:22px;border-radius:50%;background:var(--white)}
  .brand__name{font-weight:800;font-size:27px;color:var(--white);white-space:nowrap}

  .postcard__body{
    position:absolute;left:19px;
    font-size:13.2px;
    line-height:16.1px;
    white-space:nowrap;
  }
  .postcard__body--intro{top:192px}
  .postcard__body--pitch{top:282px}
  .postcard__body b{font-weight:800}

  .postcard__claim{
    position:absolute;left:18px;top:389px;
    color:var(--heading-blue);
    font-weight:800;
    font-size:17.5px;
    line-height:22.5px;
    white-space:nowrap;
  }
  .postcard__invite{
    position:absolute;left:19px;top:437px;
    font-family:"Roboto Condensed",sans-serif;
    font-weight:700;
    color:var(--accent-blue);
    font-size:13.6px;
    white-space:nowrap;
  }
  .postcard__button{
    position:absolute;left:74px;top:469px;
    width:292px;height:20px;border-radius:10px;
    background:var(--button);
    color:var(--white);
    font-family:"Lato",sans-serif;
    font-size:12.6px;
    line-height:20px;
    text-align:center;
  }
  .postcard__fineprint{
    position:absolute;left:74px;top:493px;width:292px;
    text-align:center;
    font-family:"Lato",sans-serif;
    font-size:12.2px;
    white-space:nowrap;
  }
  .postcard__fineprint span{color:var(--accent-blue)}

  .signup{
    position:absolute;left:455px;width:204px;
    text-align:center;
    color:var(--white);
    font-family:"Roboto Condensed",sans-serif;
    line-height:1;
  }
  .signup__prompt{font-size:18px;color:#e6f6fc}
  .signup__url{font-size:23px;font-weight:700;margin-top:7px}
  .signup__join{font-family:"Mulish",sans-serif;font-weight:800}
  .signup--front{top:198px}
  .signup--front .signup__join{font-size:39px;line-height:42px;margin-top:6px}
  .signup--back{top:191px}
  .signup--back .signup__join{font-size:36px;margin-top:10px;letter-spacing:.5px}
  .signup__referral{font-size:19px;line-height:24px;margin-top:7px}

  .expiry{
    position:absolute;left:519px;top:458px;width:140px;
    text-align:center;
    font-family:"Roboto Condensed",sans-serif;
    font-size:15px;
    line-height:20px;
    color:var(--ink);
  }
  .expiry b{font-weight:700;font-size:16px}
</style>
</head>
<body>

<div class="side-label side-label--front">FRONT</div>
<div class="side-label side-label--back">BACK</div>

<!-- Front side -->
<section class="postcard postcard--front">
  <svg class="postcard__shapes" width="676" height="524" viewBox="0 0 676 524">
    <defs>
      <linearGradient id="bandFront" x1="0" y1="0" x2="1" y2="1">
        <stop offset="0" stop-color="#4f92b8"/>
        <stop offset=".5" stop-color="#3f82a9"/>
        <stop offset="1" stop-color="#6aa7c8"/>
      </linearGradient>
    </defs>
    <rect x="0" y="0" width="676" height="186" fill="url(#bandFront)" role="img" aria-label="Blue-tinted mountain cliff landscape photograph"/>
    <polygon points="417,524 676,136 676,524" fill="var(--wedge)"/>
    <circle cx="557" cy="254" r="104" fill="var(--disc-ring)"/>
    <circle cx="557" cy="254" r="97" fill="var(--disc)"/>
  </svg>

  <div class="brand"><span class="brand__dot"></span><span class="brand__name">Blue Lark Gains</span></div>

  <p class="postcard__letter postcard__greeting">To My Dear Colleague,</p>
  <p class="postcard__letter postcard__favor">This week, I want you to do yourself and me a favor, okay?</p>
  <p class="postcard__letter postcard__ask">I want you to ask your boss for a $100,000 per year salary increase.<br>If the answer is no then I want you to “give yourself” a</p>
  <p class="postcard__headline">$10,000 per month pay increase RIGHT NOW!</p>

  <p class="postcard__body postcard__body--intro">The opportunity to make 6-7 figures using SIMPLE online systems<br>is exploding right before your eyes. Why aren’t you paying<br>attention? Is It because you don’t have any idea how to<br>earn money online?&nbsp; Or are you intimidated by the thought<br>of it because you’re not tech-savvy?</p>
  <p class="postcard__body postcard__body--pitch">Throw any negative thoughts out of your mind and let us help<br>you build a <b>$100,000 + yearly income</b> that runs on automatic.<br>We’re not promising a million dollars overnight or that you’ll<br>be able to quit your job tomorrow, BUT if an extra <b>$10,000 per<br>month</b> would help you reach your goals, then you should<br>take action today!</p>

  <p class="postcard__claim">OUR SIMPLE IS SO EASY TO USE, A FIFTH GRADER<br>COULD BE SUCCESSFUL!</p>
  <p class="postcard__invite">We’re so sure you will be successful with our system that we are inviting you to</p>
  <p class="postcard__button">GET STARTED TODAY FOR FREE!!!</p>
  <p class="postcard__fineprint">That’s right...for <span>FREE!</span> No credit card is required.</p>

  <div class="signup signup--front">
    <p class="signup__prompt">GO SIGN UP NOW</p>
    <p class="signup__url">www.qmvhub.com</p>
    <p class="signup__join">JOIN<br>FREE</p>
  </div>

  <p class="expiry">Free offer expires in<br><b>48 hours!!!</b></p>
</section>

<!-- Back side -->
<section class="postcard postcard--back">
  <svg class="postcard__shapes" width="676" height="524" viewBox="0 0 676 524">
    <defs>
      <linearGradient id="bandBack" x1="0" y1="0" x2="1" y2="1">
        <stop offset="0" stop-color="#4f92b8"/>
        <stop offset=".5" stop-color="#3f82a9"/>
        <stop offset="1" stop-color="#6aa7c8"/>
      </linearGradient>
    </defs>
    <rect x="0" y="0" width="676" height="186" fill="url(#bandBack)" role="img" aria-label="Blue-tinted mountain cliff landscape photograph"/>
    <polygon points="417,524 676,136 676,524" fill="var(--wedge)"/>
    <circle cx="557" cy="254" r="104" fill="var(--disc-ring)"/>
    <circle cx="557" cy="254" r="97" fill="var(--disc)"/>
  </svg>

  <div class="brand"><span class="brand__dot"></span><span class="brand__name">Blue Lark Gains</span></div>

  <p class="postcard__letter postcard__greeting">To My Dear Colleague,</p>
  <p class="postcard__letter postcard__favor">This week, I want you to do yourself and me a favor, okay?</p>
  <p class="postcard__letter postcard__ask">I want you to ask your boss for a $100,000 per year salary increase.<br>If the answer is no then I want you to “give yourself” a</p>
  <p class="postcard__headline">$10,000 per month pay increase RIGHT NOW!</p>

  <p class="postcard__body postcard__body--intro">The opportunity to make 6-7 figures using SIMPLE online systems<br>is exploding right before your eyes. Why aren’t you paying<br>attention? Is It because you don’t have any idea how to<br>earn money online?&nbsp; Or are you intimidated by the thought<br>of it because you’re not tech-savvy?</p>
  <p class="postcard__body postcard__body--pitch">Throw any negative thoughts out of your mind and let us help<br>you build a <b>$100,000 + yearly income</b> that runs on automatic.<br>We’re not promising a million dollars overnight or that you’ll<br>be able to quit your job tomorrow, BUT if an extra <b>$10,000 per<br>month</b> would help you reach your goals, then you should<br>take action today!</p>

  <p class="postcard__claim">OUR SIMPLE IS SO EASY TO USE, A FIFTH GRADER<br>COULD BE SUCCESSFUL!</p>
  <p class="postcard__invite">We’re so sure you will be successful with our system that we are inviting you to</p>
  <p class="postcard__button">GET STARTED TODAY FOR FREE!!!</p>
  <p class="postcard__fineprint">That’s right...for <span>FREE!</span> No credit card is required.</p>

  <div class="signup signup--back">
    <p class="signup__prompt">GO SIGN UP NOW</p>
    <p class="signup__url">www.qmvhub.com</p>
    <p class="signup__join">JOINFREE</p>
    <p class="signup__referral">Enter Referral ID#<br>KV-R8057</p>
  </div>

  <p class="expiry">Free offer expires in<br><b>48 hours!!!</b></p>
</section>

</body>
</html>
```